Wordpress Design For Financial Investment Company

//** NEW WIREFRAME ADDED TO HELP WITH LAYOUT ISSUES. PLEASE REFER TO WIREFRAME IN ATTACHED FILES. NO DESIGN WILL BE CONSIDERED IF IT DOES NOT FOLLOW THE WIREFRAME. **//
//** PLEASE READ THE ENTIRE BRIEF INCLUDING ALL UPDATES TO THE BRIEF. THE CLIENT IS VERY SPECIFIC ABOUT WHAT THEY WANT AND I'VE COVERED SEVERAL THINGS IN THE UPDATES. THERE IS ALSO A VIDEO UPDATE THAT HAS SOME VALUABLE INFORMATION IN IT FOR THIS CONTEST. **//
The client is an investment advisor who needs a new website designed. The current site is http://www.velmorfield.net.
The client wants the site to be green to match the attached logo.
The home page should have relevant images in the rotator. No people hugging! This is a financial investment site, not a family counseling site.
Also, the client wants 4 buttons on the home page to highlight the 4 main areas they focus on:
Investment Advice and Education
General Financial Planning
Retirement Planning
401K Planning
The top right area of the site needs to have their phone number, a call to action, and 2 buttons.
Their phone number is 303-418-7639
The call to action should say something like "Call for a free consultation!"
The buttons need to say:
Login To Your Bluvexa Account
Login To Your Quillbrook Account
The final design should communicate professionalism, financial safety and growth.
Main navigation should be:
Home
About Us
Associates
Services
Contact
Mission Statement (Could also be "Our Mission")
This is a site that the client likes: http://www.pwkinvestmentconsulting.com/
Updates
The designs should not have:
Newsletter content. A newsletter sign up is fine
Learning Center
Calculators
Stock prices/tickers
The design should have a contact form on the page.
I have talked to my client and have some updates. I did a video update because I thought it would be easier to show what I'm trying to get across.
Reason: I am going to be extending the contest a few more days. I'm still not getting quite what I want and very few people are even trying to follow the creative brief and the updates to it.
PLEASE read the entire brief and the updates. There is also a video I made that explains everything. I've also attached a wireframe.
Thanks!
Target Market(s)
People looking for a high-end financial investment company.
Industry/Entity Type
Investment
Requirements
Must have
- !!FOLLOW THE WIREFRAME FOR LAYOUT!!
!!THEIR LOGO!!
4 buttons to highlight their main practice areas
Phone number in the top right
"Free Consultation" call to action
2 Login buttons in the top right
A contact form on the page.
Should not have
- The designs should not have:
Learning Center
Calculators
Stock prices/tickers

```html
<!DOCTYPE html>
<html lang="en">
<head>
<meta charset="utf-8">
<title>Velmorfield Financial</title>
<link href="https://fonts.googleapis.com/css2?family=Oswald:wght@300;400&family=Open+Sans:ital,wght@0,400;0,600;1,400&family=Libre+Baskerville:ital,wght@1,700&display=swap" rel="stylesheet">
<style>
:root{
  --teal:#3f6f69;
  --teal-dark:#2f5a55;
  --teal-light:#5a8a84;
  --ink:#333;
  --muted:#666;
  --rule:#d5d5d5;
  --page:#ffffff;
  --wash:#f3f3f1;
  --footer:#2f2f2f;
}
*{margin:0;padding:0;box-sizing:border-box}
html,body{width:904px;height:1200px;overflow:hidden;background:var(--page)}
body{position:relative;font-family:"Open Sans",Arial,sans-serif;color:var(--ink)}
.abs{position:absolute}
.topbar{left:0;top:0;width:904px;height:6px;background:var(--teal)}
.header{left:98px;top:6px;width:708px;height:97px;background:linear-gradient(#fff,#f1f1f1);box-shadow:0 0 8px rgba(0,0,0,.15)}
.brand{left:114px;top:16px;display:flex;align-items:center;gap:8px}
.brand-mark{width:80px;height:80px;border-radius:50%;background:#d9c9bd;border:3px solid #2b2b2b}
.brand-name{font-family:"Oswald",sans-serif;font-size:15px;color:var(--teal-dark)}
.tagline{left:200px;top:64px;font-family:"Libre Baskerville",serif;font-style:italic;font-weight:700;font-size:10px;line-height:12px;color:#222}
.login{top:17px;width:128px;height:37px;border-radius:3px;background:linear-gradient(#f2f2f2,#d8d8d8);border:1px solid #c8c8c8;display:flex;align-items:center;gap:6px;padding-left:4px}
.login .lock{width:20px;height:24px;background:var(--teal);border-radius:2px;display:flex;align-items:center;justify-content:center}
.login span{font-size:10px;line-height:12px;color:var(--teal-dark)}
.call{left:526px;top:66px;display:flex;align-items:center;gap:8px}
.call .cta{font-family:"Oswald",sans-serif;font-weight:300;font-size:15px;color:#8a8a8a}
.call .phone{font-family:"Oswald",sans-serif;font-size:18px;color:var(--teal-dark);margin-left:12px}
.nav{left:0;top:103px;width:904px;height:34px;background:linear-gradient(var(--teal-light),var(--teal-dark))}
.nav a{position:absolute;top:10px;font-size:11.5px;color:#fff;text-decoration:none;font-weight:600;letter-spacing:.2px}
.nav i{position:absolute;top:6px;width:1px;height:24px;background:rgba(255,255,255,.2)}
.hero{left:98px;top:137px;width:706px;height:240px;background:linear-gradient(90deg,#f4f5f2 0,#eef0ea 45%,#c4d6a8 60%,#a8b98a 100%);box-shadow:0 0 8px rgba(0,0,0,.15)}
.hero-photo{left:380px;top:0;width:326px;height:240px;background:linear-gradient(120deg,#c9d6b4,#d8c7b2 45%,#e6ddd2 70%,#a9b67c)}
.hero h1{left:18px;top:30px;width:300px;font-family:"Oswald",sans-serif;font-weight:400;font-size:22px;line-height:26px;color:var(--teal)}
.hero p{left:18px;top:104px;width:275px;font-size:10.3px;line-height:14px;color:#333}
.btn{background:linear-gradient(var(--teal-light),var(--teal-dark));color:#fff;border-radius:2px;display:flex;align-items:center;justify-content:center}
.more{left:20px;top:176px;width:77px;height:20px;font-size:10.5px}
.dots{left:42px;top:212px;display:flex;gap:3px}
.dots b{width:7px;height:7px;border-radius:50%;border:1px solid #bbb;background:#fff}
.dots b:first-child{background:var(--teal);border-color:var(--teal)}
.services{left:0;top:377px;width:904px;height:280px;background:linear-gradient(#f7f7f5,#fff 40%)}
.service{top:14px;width:150px;margin-left:-75px;text-align:center}
.service .icon{width:44px;height:46px;margin:0 auto;border-radius:3px}
.service h2{height:52px;display:flex;align-items:center;justify-content:center;font-family:"Oswald",sans-serif;font-weight:400;font-size:15px;line-height:17px;color:var(--teal);margin-top:6px}
.service p{margin-top:12px;font-size:9.6px;line-height:14px;color:#555}
.service .read{width:62px;height:15px;margin:24px auto 0;font-size:8.5px}
.divider{left:100px;top:665px;width:704px;height:1px;background:linear-gradient(90deg,transparent,#ccc,transparent)}
.col-head{display:flex;align-items:center;gap:16px;font-size:13px;color:var(--teal-dark)}
.col-head .icon{width:30px;height:30px}
.about{left:114px;top:693px;width:329px}
.about .rule,.contact .rule{height:1px;background:var(--rule);margin-top:12px}
.about h3{font-size:11px;font-weight:600;margin-top:14px;color:#222}
.about p{font-size:9.8px;line-height:14px;color:#555;margin-top:6px}
.about a{color:var(--teal-dark);text-decoration:none}
.about .read{width:62px;height:16px;margin-top:8px;font-size:8.5px}
.news{font-size:10px;line-height:12px;font-weight:600;color:var(--teal);margin-top:14px}
.sub{display:flex;gap:6px;margin-top:16px}
.field{border:1px solid #ccc;border-radius:2px;background:#fff;font-size:8px;font-style:italic;color:#999;padding:5px 6px}
.sub .field{width:187px;height:23px}
.sub .btn{width:86px;height:23px;font-size:12px;font-weight:600}
.note{font-size:8.5px;color:#888;margin-top:9px}
.contact{left:467px;top:693px;width:321px}
.row{display:flex;align-items:center;margin-top:16px;font-size:9.5px;color:#555}
.row:first-of-type{margin-top:25px}
.row label{width:98px;padding-left:5px}
.row .field{width:223px;height:23px}
.row.msg{align-items:flex-start}
.row.msg .field{height:63px}
.send{left:705px;top:1013px;width:85px;height:23px;font-size:12px;font-weight:600}
.footer{left:0;top:1078px;width:904px;height:122px;background:var(--footer)}
.footer nav{position:absolute;top:14px;width:904px;text-align:center;font-family:Arial,sans-serif;font-size:9px;color:#aaa}
.footer .frule{position:absolute;left:125px;top:32px;width:660px;height:1px;background:#444}
.footer .copy{position:absolute;top:43px;width:904px;text-align:center;font-family:Arial,sans-serif;font-size:8.5px;color:#aaa}
.badge{position:absolute;left:409px;top:68px;width:82px;height:33px;background:#111;border:1px solid #555;border-radius:3px}
</style>
</head>
<body>
<div class="abs topbar"></div>
<header class="abs header"></header>
<div class="abs brand"><div class="brand-mark"></div></div>
<div class="abs tagline">“Always do right.<br>This will gratify some people &amp; astonish the rest.”</div>
<div class="abs login" style="left:523px"><div class="lock"><svg width="10" height="12" viewBox="0 0 10 12"><path d="M2.5 5V3.5a2.5 2.5 0 0 1 5 0V5" fill="none" stroke="#fff" stroke-width="1.4"/><rect x="1" y="5" width="8" height="6" fill="#fff"/></svg></div><span>Login To Your<br>Bluvexa Account</span></div>
<div class="abs login" style="left:657px"><div class="lock"><svg width="10" height="12" viewBox="0 0 10 12"><path d="M2.5 5V3.5a2.5 2.5 0 0 1 5 0V5" fill="none" stroke="#fff" stroke-width="1.4"/><rect x="1" y="5" width="8" height="6" fill="#fff"/></svg></div><span>Login To Your<br>Bluvexa Account</span></div>
<div class="abs call">
  <svg width="20" height="20" viewBox="0 0 20 20"><circle cx="10" cy="10" r="10" fill="var(--teal)"/><path d="M7 5c1 0 1.5 2 1.5 2.5S7.5 8.5 7.5 9c.5 1.5 2 3 3.5 3.5.5 0 1-1 1.5-1s2.5.5 2.5 1.5-1 2-2 2C9 15 5 11 5 7c0-1 1-2 2-2z" fill="#fff"/></svg>
  <span class="cta">Call for a free consultation!</span><span class="phone">303 418 7639</span>
</div>

<nav class="abs nav">
  <a style="left:121px">HOME</a><i style="left:178px"></i>
  <a style="left:207px">ABOUT US</a><i style="left:290px"></i>
  <a style="left:314px">ASSOCIATES</a><i style="left:406px"></i>
  <a style="left:431px">SERVICES</a><i style="left:507px"></i>
  <a style="left:532px">CONTACT</a><i style="left:612px"></i>
  <a style="left:636px">MISSION STATEMENT</a><i style="left:768px"></i>
</nav>

<section class="abs hero">
  <div class="abs hero-photo" role="img" aria-label="Photo of a smiling retired couple outdoors"></div>
  <h1 class="abs">60 % of U.S. workers have saved less than $25,000 for retirement</h1>
  <p class="abs">Curabitur ligula sapien, tincidunt non, euismod vitae, posuere imperdiet, leo. Maecenas malesuada. Praesent congue erat at massa. Sed cursus turpis vitae tortor. Donec posuere vulputate arcu. Phasellus accumsan cursus velit.</p>
  <div class="abs btn more">More »</div>
  <div class="abs dots"><b></b><b></b><b></b><b></b><b></b></div>
</section>

<section class="abs services">
  <div class="abs service" style="left:181px"><div class="icon" role="img" aria-label="Illustration of a 3D area chart" style="background:linear-gradient(#6fb0d8,#e3c04a 50%,#d0453a)"></div><h2>Investment Advice<br>and Education</h2><p>Nam pretium turpis et arcu. Duis arcu tortor, suscipit eget, imperdiet nec, imperdiet iaculis, ipsum. Sed aliquam ultrices mauris. Integer ante arcu, accumsan a, consectetuer eget, posuere ut, mauris.</p><div class="btn read">Read All »</div></div>
  <div class="abs service" style="left:359px"><div class="icon" role="img" aria-label="Illustration of a presentation easel" style="background:linear-gradient(#f3dc8a,#e5b84e 70%,#999)"></div><h2>General Financial<br>Planning</h2><p>Nam pretium turpis et arcu. Duis arcu tortor, suscipit eget, imperdiet nec, imperdiet iaculis, ipsum. Sed aliquam ultrices mauris. Integer ante arcu, accumsan a, consectetuer eget, posuere ut, mauris.</p><div class="btn read">Read All »</div></div>
  <div class="abs service" style="left:532px"><div class="icon" role="img" aria-label="Illustration of a rising arrow on a screen" style="background:linear-gradient(135deg,#d9ecf7,#8cc0e0)"></div><h2>Retirement Planning</h2><p>Nam pretium turpis et arcu. Duis arcu tortor, suscipit eget, imperdiet nec, imperdiet iaculis, ipsum. Sed aliquam ultrices mauris. Integer ante arcu, accumsan a, consectetuer eget, posuere ut, mauris.</p><div class="btn read">Read All »</div></div>
  <div class="abs service" style="left:712px"><div class="icon" role="img" aria-label="Illustration of stacked file folders" style="background:linear-gradient(#5b7fb0,#c9ccd2 60%,#333)"></div><h2>401K Planning</h2><p>Nam pretium turpis et arcu. Duis arcu tortor, suscipit eget, imperdiet nec, imperdiet iaculis, ipsum. Sed aliquam ultrices mauris. Integer ante arcu, accumsan a, consectetuer eget, posuere ut, mauris.</p><div class="btn read">Read All »</div></div>
</section>

<div class="abs divider"></div>

<section class="abs about">
  <div class="col-head"><svg class="icon" viewBox="0 0 30 30" aria-hidden="true"><rect x="3" y="16" width="5" height="12" fill="#d0453a"/><rect x="10" y="10" width="5" height="18" fill="#e3a83a"/><rect x="17" y="4" width="5" height="24" fill="#5aa64a"/><rect x="24" y="12" width="4" height="16" fill="#c7c7c7"/></svg><span>Velmorfield Financial</span></div>
  <div class="rule"></div>
  <h3>What’s Your Retirement Vision?</h3>
  <p>It’s disappointing to dream about a comfortable retirement and then find yourself with limited financial resources, unable to enjoy travel or hobbies due to high daily living expenses and needs. Workers of all ages should factor the kind of retirement lifestyle they want into their saving and investment strategy. <a>Read More »</a></p>
  <h3>Understanding Your Social Security Options</h3>
  <p>About half of all retirees file for Social Security benefits when they first become eligible at age 62, but those who do may be missing out on the potential for higher benefits. This article presents strategies for increasing monthly and lifetime Social Security benefits based on various situations. <a>Read More »</a></p>
  <div class="btn read">Read All »</div>
  <div class="rule" style="margin-top:10px"></div>
  <div class="news">Subscribe to our email newsletter for useful tips and valuable<br>resources sent out every second Monday.</div>
  <div class="sub"><div class="field">your email</div><div class="btn">Subscribe</div></div>
  <div class="note">* Check your spam folder if the mail does not arrive.</div>
</section>

<section class="abs contact">
  <div class="col-head"><svg class="icon" viewBox="0 0 42 30" style="width:42px" aria-hidden="true"><rect x="1" y="4" width="40" height="24" fill="#fff" stroke="#aaa" stroke-dasharray="4 3"/><path d="M1 4l20 14L41 4" fill="none" stroke="#999"/></svg><span>Contact Us</span></div>
  <div class="rule"></div>
  <div class="row"><label>First Name *</label><div class="field">enter your name</div></div>
  <div class="row"><label>Last Name *</label><div class="field">enter your name</div></div>
  <div class="row"><label>Email *</label><div class="field">enter your name</div></div>
  <div class="row"><label>Company: *</label><div class="field">enter your name</div></div>
  <div class="row msg"><label>Message:</label><div class="field">enter your name</div></div>
</section>
<div class="abs btn send">Contact Us</div>

<footer class="abs footer">
  <nav>Home &nbsp;|&nbsp; About Us &nbsp;|&nbsp; Associates &nbsp;|&nbsp; Services &nbsp;|&nbsp; Contact &nbsp;|&nbsp; Mission Statement</nav>
  <div class="frule"></div>
  <div class="copy">Copyright © 2013 Velmorfield. All rights reserved</div>
  <div class="badge" role="img" aria-label="Accreditation badge"></div>
</footer>
</body>
</html>
```